Web Re-Design for African Art Gallery

Introduction
We are an art gallery carrying artworks by contemporary African artists. We require a new, more modern website for our gallery.
The website idea. The key words we’d like to use to describe our website are - elegant, simple, uncluttered, easy to navigate, classy, interesting.
We’d like a website that is as uncluttered as possible; a simple, elegant website that lets viewers carry out the business of viewing our artworks online as easily as possible. A web site that is adventurous and arty without being complicated.
Our logo is a monochrome dark grey colour but this should not affect the colour scheme of the website. We are also open to a new logo if it is decidedly better than what we have at present, and would be willing to pay additionally for it if we take it.
Our audience is international. Art collectors worldwide looking for contemporary art. We do not want any African themed design.
Sections
The home page will have various sections – Artists, New Works, Publication, Mailing list, Exhibitions
Below are a list of gallery websites we like.
http://www.tarvelqonsik.example/
http://www.pembrowgallery.example/
http://www.dalefrunkwater.example/
http://www.quillopraxa.example/exhibitions/2011-12-13_velvet-arcades/
http://www.zot.vrbn.example/index.html
Requirement
We'd like a a home page template as well as a template for the sections in HTML.
We do not have a regular coder so we'd be happy to have the winning designer carry on with fitting the rest of the site to the template if the price is right.
Our present website is www.moonfernstudio.example. feel free to get logo, artwork pictures and any other material you might need from there.
Thanks

```html
<!DOCTYPE html>
<html lang="en">
<head>
<meta charset="utf-8">
<title>Moonfern Studio</title>
<link href="https://fonts.googleapis.com/css2?family=Open+Sans:wght@400;600&display=swap" rel="stylesheet">
<style>
:root{
  --orange:#e0661b;
  --band:#fdb515;
  --ink:#222;
  --body:#8a8a8a;
  --rule:#d6d6d6;
  --chip:#e9e9e9;
  --footer:#efefef;
  --navbg:#f7f7f7;
  --active:#c9c9c9;
}
*{box-sizing:border-box;margin:0;padding:0}
html,body{width:826px;height:1200px;overflow:hidden;background:#fff}
body{position:relative;font-family:"Open Sans",Arial,sans-serif;color:var(--ink)}
.abs{position:absolute}
.site-nav{left:0;top:0;width:826px;height:45px;background:var(--navbg);border-bottom:1px dashed var(--rule)}
.site-nav a{position:absolute;top:0;height:45px;line-height:48px;font-size:13px;color:var(--orange);text-decoration:none}
.site-nav a.active{background:var(--active);color:#333;width:71px;text-align:center}
.brand{left:17px;top:71px;width:176px;height:70px;border:2px solid #444;box-shadow:3px 3px 4px rgba(0,0,0,.35);display:flex;align-items:center;justify-content:center;gap:8px;background:#fff}
.brand-mark{width:12px;height:12px;background:#444}
.brand-name{font-size:18px;font-weight:600;color:#444}
.share{left:623px;top:84px;font-size:13px}
.social{top:83px;width:16px;height:16px;background:#7a7a7a;border-radius:2px}
.search{left:620px;top:121px;width:146px;height:19px;border:1px solid #ccc;border-radius:10px;box-shadow:inset 1px 1px 2px rgba(0,0,0,.2);font-size:9px;color:#666;padding:3px 10px}
.search-go{left:764px;top:120px;width:21px;height:21px;border-radius:50%;background:#111;color:#fff;font-size:10px;text-align:center;line-height:20px}
.hero{left:17px;top:167px;width:792px;height:258px;border-radius:6px;box-shadow:0 3px 5px rgba(0,0,0,.2);
  background:
    radial-gradient(ellipse 170px 110px at 50% 60%,#f0600e 0%,#f37a1c 45%,rgba(246,150,40,0) 100%),
    radial-gradient(ellipse 330px 170px at 47% 45%,rgba(245,140,35,.9) 0%,rgba(248,175,60,.6) 50%,rgba(250,220,140,0) 100%),
    radial-gradient(ellipse 120px 90px at 12% 15%,rgba(247,170,45,.7),rgba(247,170,45,0)),
    linear-gradient(90deg,#f8e3a4 0%,#fdf4de 30%,#fbeab7 70%,#f8dd8e 100%)}
.hero-arrow{top:246px;width:23px;height:92px;background:rgba(255,255,255,.85)}
.band{left:22px;width:540px;height:27px;background:linear-gradient(90deg,var(--band) 70%,rgba(253,181,21,0));border-bottom:1px dashed var(--rule);color:#fff;font-size:16px;font-weight:400;line-height:27px;padding-left:16px;display:flex;align-items:center;gap:8px}
.hand{width:20px;height:20px;flex:none}
.thumb{width:160px;height:100px;border:1px solid #ccc;box-shadow:0 10px 8px -6px rgba(0,0,0,.15)}
.pill{left:25px;top:621px;width:78px;height:19px;border:1px solid #ccc;border-radius:10px;font-size:10px;color:#777;text-align:center;line-height:17px;background:#fafafa}
.artists{left:25px;top:690px;width:537px;height:208px;border:1px solid #e2e2e2;background:#fff}
.artist-col{list-style:none;top:701px;font-size:10px;line-height:20.2px}
.artist-col li::before{content:"›";font-weight:600;margin-right:7px}
.expo{top:947px;height:107px;border:1px solid #ccc}
.aside-title{left:586px;font-size:16px;font-weight:400}
.news-head{left:589px;font-size:11px;font-weight:400}
.news-body{left:588px;width:220px;font-size:8.5px;line-height:12.8px;color:var(--body)}
.posted{left:587px;width:136px;height:18px;background:var(--chip);font-size:10.5px;padding-left:6px;line-height:18px}
.rule{left:590px;width:215px;height:1px;background:var(--rule)}
.more{font-size:10px;right:24px}
.pub{width:107px;height:75px;border:1px solid #333}
.footer{left:4px;top:1108px;width:822px;height:92px;background:var(--footer)}
.foot-txt{font-size:8.5px;line-height:17px}
</style>
</head>
<body>
<svg width="0" height="0" style="position:absolute">
  <symbol id="hand-icon" viewBox="0 0 20 20">
    <g fill="#fff" stroke="#fff" stroke-linecap="round">
      <path d="M6 10 Q6 17 11 18 Q16 18 16 12 L16 9 Q14 8 13 11 L13 10 L7 9 Z" stroke-width="1"/>
      <line x1="7.5" y1="10" x2="5.5" y2="3.5" stroke-width="2.2"/>
      <line x1="9.5" y1="10" x2="8.8" y2="2" stroke-width="2.2"/>
      <line x1="11.5" y1="10" x2="12" y2="2.8" stroke-width="2.2"/>
      <line x1="13" y1="11" x2="14.8" y2="4.5" stroke-width="2.2"/>
      <line x1="15.5" y1="11" x2="18" y2="8" stroke-width="2.2"/>
    </g>
  </symbol>
</svg>

<nav class="abs site-nav">
  <a class="active" href="#" style="left:28px">HOME</a>
  <a href="#" style="left:127px">ARTICLES</a>
  <a href="#" style="left:224px">PROFILES</a>
  <a href="#" style="left:321px">CONTACT</a>
  <a href="#" style="left:421px">LIVE CHAT</a>
  <a href="#" style="left:523px">GALLERY</a>
  <a href="#" style="left:618px">EXHIBITIONS</a>
  <a href="#" style="left:733px">MF-MAIL</a>
</nav>

<div class="abs brand"><span class="brand-mark"></span><span class="brand-name">Moonfern Studio</span></div>

<div class="abs share">Shared With</div>
<span class="abs social" style="left:702px"></span>
<span class="abs social" style="left:723px"></span>
<span class="abs social" style="left:744px"></span>
<span class="abs social" style="left:765px"></span>
<div class="abs search">type your word here</div>
<div class="abs search-go">go</div>

<div class="abs hero" role="img" aria-label="Large painted orange flower on a pale yellow wash"></div>
<div class="abs hero-arrow" style="left:19px"><svg width="23" height="92"><polyline points="15,20 4,46 15,72" fill="none" stroke="#222" stroke-width="1.2"/></svg></div>
<div class="abs hero-arrow" style="left:783px"><svg width="23" height="92"><polyline points="8,20 19,46 8,72" fill="none" stroke="#222" stroke-width="1.2"/></svg></div>

<h2 class="abs band" style="top:458px">Some of Our New Work<svg class="hand"><use href="#hand-icon"/></svg></h2>
<div class="abs thumb" role="img" aria-label="Colourful mixed-media painting" style="left:26px;top:495px;background:linear-gradient(135deg,#d9b08a,#b7a7c9,#e6cf9a)"></div>
<div class="abs thumb" role="img" aria-label="Green abstract painting with dark circular form" style="left:202px;top:495px;background:linear-gradient(135deg,#7e9a4c,#3f5b2a,#9fb45e)"></div>
<div class="abs thumb" role="img" aria-label="Golden painting with a blue bird" style="left:376px;top:495px;background:linear-gradient(135deg,#c99a4f,#e0bd6a,#7f97b6)"></div>
<div class="abs pill">view more</div>

<h2 class="abs band" style="top:660px">Artists<svg class="hand"><use href="#hand-icon"/></svg></h2>
<div class="abs artists"></div>
<ul class="abs artist-col" style="left:44px">
  <li>Tobin Varrecke</li><li>Oriel Plaskett</li><li>Corvin Dallow</li><li>Ema Strelby</li><li>Lorcan Tivvy</li><li>Pell Quorrin</li><li>Niva Selk</li><li>Aldous Frenn</li><li>.Mirel Tashcombe</li>
</ul>
<ul class="abs artist-col" style="left:164px">
  <li>Rune Kaspell</li><li>Hollis Venbrook</li><li>Iver Lottam</li><li>Sorel Quintane</li><li>Bram Okkeley</li><li>Dace Wimbury</li><li>Fenwick Altravelle</li><li>Juno Perrit</li><li>Casimir Rendolow</li>
</ul>
<ul class="abs artist-col" style="left:293px">
  <li>Tam Orlish</li><li>Edwin Marrowfield</li><li>Lise Dombray</li><li>Vesna Clotheroe</li><li>Elio Brantswick</li><li>Kit Morvane</li><li>Anselm Greyholt</li><li>Aldous Frenn</li><li>Ruan Pelligrew</li>
</ul>
<ul class="abs artist-col" style="left:423px">
  <li>Wren Castamir</li><li>Gideon Flurry</li><li>Osric Talbenn</li><li>Marek Windholm</li><li>Ilsa Fenmoor</li><li>Perrin Ashgrove</li><li>Tavish Remmer</li><li>Quentin Harrowmere</li><li>Delia Brannock</li>
</ul>

<h2 class="abs band" style="top:905px;left:20px;padding-left:12px">Exhibitions<svg class="hand"><use href="#hand-icon"/></svg></h2>
<div class="abs expo" role="img" aria-label="Geometric abstract composition" style="left:22px;width:170px;background:linear-gradient(135deg,#efe3c4,#d9b673,#9fb0c7)"></div>
<div class="abs expo" role="img" aria-label="Grid of exhibition photographs" style="left:198px;width:171px;background:linear-gradient(135deg,#8a7aa6,#a4663f,#9a9a9a)"></div>
<div class="abs expo" role="img" aria-label="White gallery room with hung works" style="left:376px;width:170px;background:linear-gradient(180deg,#f2f2f2 60%,#c99a6a)"></div>

<h2 class="abs aside-title" style="top:463px">Newsletter Mailing list</h2>

<h3 class="abs news-head" style="top:503px">Heading goes here</h3>
<p class="abs news-body" style="top:522px">The only way to success is through the right path and that’s what we provide you. None of the other compa-nies has the result we do.</p>
<div class="abs posted" style="top:566px">Posted on&nbsp; 25.Jan.2012</div>

<h3 class="abs news-head" style="top:601px">Heading goes here</h3>
<p class="abs news-body" style="top:621px">The only way to success is through the right path and that’s what we provide you. None of the other compa-nies has the result we do.</p>
<div class="abs posted" style="top:663px">Posted on&nbsp; 25.Jan.2012</div>

<h3 class="abs news-head" style="top:707px">Heading goes here</h3>
<p class="abs news-body" style="top:726px">The only way to success is through the right path and that’s what we provide you. None of the other compa-nies has the result we do.</p>
<div class="abs posted" style="top:769px">Posted on&nbsp; 25.Jan.2012</div>

<div class="abs rule" style="top:808px"></div>
<div class="abs more" style="top:809px">view more</div>

<h2 class="abs aside-title" style="top:840px">Publication</h2>
<div class="abs pub" role="img" aria-label="Publication cover, warm abstract" style="left:587px;top:868px;background:linear-gradient(135deg,#e0a23a,#7b8f3c)"></div>
<div class="abs pub" role="img" aria-label="Publication cover, street painting" style="left:702px;top:868px;background:linear-gradient(135deg,#3a5a7a,#b88a6a)"></div>
<div class="abs pub" role="img" aria-label="Publication cover, dark still life" style="left:587px;top:955px;background:linear-gradient(135deg,#3a1e14,#8a5a3a)"></div>
<div class="abs pub" role="img" aria-label="Publication cover, landscape with figures" style="left:702px;top:955px;background:linear-gradient(135deg,#6a8ab8,#d8b88a)"></div>
<div class="abs rule" style="top:1043px"></div>
<div class="abs more" style="top:1044px">view more</div>

<footer class="abs footer"></footer>
<div class="abs foot-txt" style="left:26px;top:1124px">Copyright © 2012 Company Name |&nbsp;&nbsp; All right reserved<br>Privacy Policy&nbsp; | &nbsp;Terms &amp; Conditions</div>
<div class="abs foot-txt" style="left:437px;top:1124px">Home&nbsp; | &nbsp;About Us&nbsp; | &nbsp;Contact Us&nbsp; | &nbsp;Live Chat&nbsp; | &nbsp;Gallery&nbsp; | &nbsp;Articles&nbsp; | &nbsp;Profiles&nbsp; | &nbsp;MF-Email</div>
</body>
</html>
```